Zanquorra Business Card Design

Zanquorra is a small and new restaurant/ bar location in Hong Kong. The name "Djibouti" derives from an African country. There is no specific reason behind other than the fact, that the bar is somewhat inspired by African elements (only inspired but not purely based on African cuisine etc.).

The bar is somewhat a fusion of African, Mediterranean and Oriental (Old French Vietnam) elements.

However, it is very imperative to stress, that the overall look and feel of Zanquorra is a very high end cocktail lounge/ bar location. The bar is tucked away in a hidden alley, so people will have to know about it. The idea is to send the consumer off in an Escape or hidden remote location where they are at ease in a hip, stylish and trendy environment.

The card needs to feel high-end.

Final logo artwork has been attached and also pictures of the bar/ restaurant itself. The logo ie monkey head cannot be modified. However, the background color and the color of the type "ZANQUORRA" can be changed.

The following details need to fit onto the business card. Of course they can be arranged to your liking:

LOGO

Colin Vey
Partner

+852 97035164
xxx@zanquorra.com
www.zanquorra.com
7C, Brennick Road, Wan Chai, Hong Kong

```html
<!DOCTYPE html>
<html lang="en">
<head>
<meta charset="utf-8">
<title>Zanquorra Business Card</title>
<link rel="stylesheet" href="https://fonts.googleapis.com/css2?family=Cinzel:wght@400;600&display=swap">
<style>
  :root {
    --stage: #5a3a26;
    --card-black: #0a0a0e;
    --glow-pink: rgba(214, 110, 190, 0.85);
    --glow-magenta: rgba(150, 50, 150, 0.85);
    --glow-blue: rgba(50, 140, 200, 0.85);
    --glow-violet: rgba(110, 70, 150, 0.75);
    --ink: #f4f0f2;
    --faint-ring: rgba(255, 255, 255, 0.12);
  }
  * { margin: 0; padding: 0; box-sizing: border-box; }
  html, body {
    width: 1200px;
    height: 1000px;
    overflow: hidden;
    background: var(--stage);
  }
  .canvas {
    position: relative;
    width: 1200px;
    height: 1000px;
  }
  .card {
    position: absolute;
    width: 592px;
    height: 379px;
    border-radius: 14px;
    overflow: hidden;
    font-family: "Cinzel", "Trajan Pro", serif;
    color: var(--ink);
    background:
      radial-gradient(ellipse 55% 60% at 50% 50%, transparent 40%, rgba(0,0,0,0.55) 100%),
      radial-gradient(ellipse 22% 24% at 16% 20%, var(--glow-pink), transparent 100%),
      radial-gradient(ellipse 28% 36% at 18% 45%, var(--glow-magenta), transparent 100%),
      radial-gradient(ellipse 30% 32% at 72% 50%, var(--glow-blue), transparent 100%),
      radial-gradient(ellipse 40% 40% at 50% 60%, var(--glow-violet), transparent 100%),
      radial-gradient(ellipse 30% 20% at 60% 12%, rgba(120, 40, 110, 0.7), transparent 100%),
      var(--card-black);
  }
  .card--front { left: 303px; top: 81px; }
  .card--back  { left: 305px; top: 562px; }

  .brand-mark {
    position: absolute;
    left: 220px;
    top: 88px;
    width: 152px;
    height: 152px;
    border-radius: 50%;
    background: #201812;
    border: 3px solid var(--ink);
  }
  .brand-name {
    position: absolute;
    left: 0;
    right: 0;
    top: 226px;
    text-align: center;
    font-size: 58px;
    font-weight: 600;
    letter-spacing: 2px;
  }

  .faint-ring {
    position: absolute;
    left: 128px;
    top: 22px;
    width: 330px;
    height: 330px;
    border-radius: 50%;
    border: 14px solid var(--faint-ring);
  }
  .holder-name {
    position: absolute;
    left: 0; right: 0;
    top: 62px;
    text-align: center;
    font-size: 46px;
    font-weight: 400;
    letter-spacing: 1px;
  }
  .holder-role {
    position: absolute;
    left: 0; right: 0;
    top: 122px;
    text-align: center;
    font-size: 26px;
    letter-spacing: 1px;
  }
  .contact-list {
    position: absolute;
    left: 50px;
    top: 210px;
    list-style: none;
    font-size: 18px;
    line-height: 23px;
  }
</style>
</head>
<body>
  <main class="canvas">
    <section class="card card--front" aria-label="Card front">
      <div class="brand-mark" role="img" aria-label="Zanquorra brand emblem area"></div>
      <h1 class="brand-name">ZANQUORRA</h1>
    </section>

    <section class="card card--back" aria-label="Card back">
      <div class="faint-ring" aria-hidden="true"></div>
      <h2 class="holder-name">Colin Vey</h2>
      <p class="holder-role">Partner</p>
      <ul class="contact-list">
        <li>+852 97035164</li>
        <li>xxx@zanquorra.com</li>
        <li>www.zanquorra.com</li>
        <li>7C, Brennick Road, Wan Chai, Hong Kong</li>
      </ul>
    </section>
  </main>
</body>
</html>
```